Premium Olive Oil Bottle Label

Need a double bottle label for our premium olive oil (front and back). Please refer to the brief attached. The label needs to incorporate the elements from the logo designs that we provide in attachment into a single design language. The front panel should capture attention and the back panel provide a story of our unique product.

Target Market(s)

US and Europe

Industry/Entity Type

Food Production

Font styles to use
Other font styles liked:
• Please refer to the Brief

Colors

Designer to choose colors to be used in the design.

Requirements
Must have
• Integrate the elements in the brief into a single premium execution.
Nice to have
• Feel free to use the provided visual elements as a base for your further creative exploration.
Should not have
• Too many colors. Please propose a restricted color palette as the bottle is black matte. The design needs to deliver premium appeal and be distinctive.

```html
<!DOCTYPE html>
<html lang="en">
<head>
<meta charset="utf-8">
<title>La Belle Colline – Extra Virgin Olive Oil Label</title>
<link href="https://fonts.googleapis.com/css2?family=Cinzel:wght@700&family=Oswald:wght@300;500&family=Cormorant+Garamond:ital,wght@1,500&family=Roboto+Condensed:wght@400&display=swap" rel="stylesheet">
<style>
  :root {
    --page: #ffffff;
    --label-black: #1c1b1a;
    --gold: #c9a45c;
    --gold-deep: #8a6a2f;
    --gold-light: #e6cf97;
    --ivory: #f2efe8;
  }
  * { margin: 0; padding: 0; box-sizing: border-box; }
  html, body {
    width: 1200px; height: 794px; overflow: hidden;
    background: var(--page);
  }
  .canvas {
    position: relative; width: 1200px; height: 794px;
  }
  .label {
    position: absolute; left: 370px; top: 57px;
    width: 460px; height: 680px;
  }
  .label-shape { position: absolute; inset: 0; }
  .label-text {
    position: absolute; left: 0; right: 0;
    text-align: center; line-height: 1;
  }
  .harvest-date {
    top: 34px; font-family: "Roboto Condensed", sans-serif;
    font-size: 14px; color: var(--gold-light); letter-spacing: 0.5px;
  }
  .ornament {
    position: absolute; left: 62px; top: 66px; width: 336px; height: 176px;
    border-radius: 50% 50% 40% 40% / 60% 60% 40% 40%;
    background: radial-gradient(ellipse at center, rgba(28,27,26,0.95) 0%, rgba(28,27,26,0.85) 30%, rgba(138,106,47,0.55) 65%, rgba(201,164,92,0.25) 100%);
  }
  .brand-name {
    font-family: "Cinzel", serif; font-weight: 700; color: var(--ivory);
  }
  .brand-le { top: 112px; font-size: 32px; }
  .brand-main { top: 148px; font-size: 50px; letter-spacing: 1px; }
  .brand-sub { top: 198px; font-size: 32px; }
  .organic {
    top: 312px; font-family: "Cinzel", serif; font-weight: 700;
    font-size: 28px; color: var(--gold); letter-spacing: 1px;
  }
  .product-line {
    top: 378px; font-family: "Oswald", sans-serif; font-weight: 300;
    font-size: 28px; color: var(--ivory); letter-spacing: 0.5px;
  }
  .product-name {
    top: 412px; font-family: "Oswald", sans-serif; font-weight: 500;
    font-size: 36px; color: var(--ivory); letter-spacing: 1px;
  }
  .seal {
    position: absolute; width: 74px; height: 74px; top: 403px;
    border: 1.5px solid var(--gold); border-radius: 50%;
    display: flex; align-items: center; justify-content: center;
    font-family: "Roboto Condensed", sans-serif; font-size: 13px;
    color: var(--ivory); text-align: center; line-height: 1.2;
  }
  .seal-left { left: 50px; }
  .seal-right { left: 336px; }
  .details {
    top: 468px; font-family: "Cormorant Garamond", serif; font-style: italic;
    font-weight: 500; font-size: 19px; color: var(--gold); line-height: 24px;
  }
  .origin {
    top: 594px; font-family: "Roboto Condensed", sans-serif;
    font-size: 15px; color: var(--ivory);
  }
  .volume {
    top: 626px; font-family: "Roboto Condensed", sans-serif;
    font-size: 13px; color: var(--ivory);
  }
</style>
</head>
<body>
<main class="canvas">
  <section class="label" aria-label="Front olive oil label">
    <svg class="label-shape" width="460" height="680" viewBox="0 0 460 680">
      <ellipse cx="230" cy="340" rx="229" ry="339" fill="var(--label-black)"/>
      <ellipse cx="230" cy="340" rx="216" ry="326" fill="none" stroke="var(--gold)" stroke-width="2.5"/>
      <path d="M150 58 Q230 40 310 58" fill="none" stroke="var(--gold)" stroke-width="1.5"/>
      <line x1="92" y1="292" x2="368" y2="292" stroke="var(--gold)" stroke-width="1.2"/>
      <rect x="225" y="287" width="10" height="10" transform="rotate(45 230 292)" fill="var(--gold)"/>
      <path d="M140 356 Q230 348 320 356" fill="none" stroke="var(--gold)" stroke-width="1.2"/>
      <line x1="150" y1="614" x2="310" y2="614" stroke="var(--gold)" stroke-width="1"/>
    </svg>

    <p class="label-text harvest-date">November 2018</p>

    <div class="ornament" role="img" aria-label="Gold filigree ornament with olive branches framing the brand name"></div>

    <p class="label-text brand-name brand-le">LA</p>
    <p class="label-text brand-name brand-main">BELLE</p>
    <p class="label-text brand-name brand-sub">COLLINE</p>

    <p class="label-text organic">Organic</p>

    <p class="label-text product-line">EXTRA VIRGIN</p>
    <p class="label-text product-name">OLIVE OIL</p>

    <div class="seal seal-left">Limited<br>Edition</div>
    <div class="seal seal-right">Late<br>Harvest</div>

    <p class="label-text details">AOC Haute-Provence<br>From Provence<br>Hand-picked<br>Single Cold-Press<br>Artisanal</p>

    <p class="label-text origin">Made in France</p>
    <p class="label-text volume">Vol 500ml / No: 123 45677</p>
  </section>
</main>
</body>
</html>
```